Mobile Recording Studio needs business cards

Open to seeing a creative design, but I want to emphasis my logo and minimize the name/title and company information. Possible a fully black background on card.

My company is a mobile sound recording studio. ok to include a my trailer (actual or cartoon) on the card. My initial thought is more straight forward, but a good design will win me over.

SPECS:
CMYK color mode
High (300ppi) raster effect.
cover bleed area
please deliver: Illustrator file with layers and a pdf at completion.

Name and info for the business card:

Dallin Perry
ADR Mixer

email: Dallin@MixVault.com

address:
248 - 5170 East Hollister
Vancouver, BC V5R 2J4

phone:
604.518.2093 office

website:
www.MixVault.com

Social: @MixVault

Photos: @TheMixVault

Industry/Entity Type

Television Production

Contact Information for Business Card

Dallin Perry
ADR Mixer

email: Dallin@MixVault.com

address:
248 - 5170 East Hollister
Vancouver, BC V5R 2J4

phone:
604.518.2093 office

website:
www.MixVault.com

Social: @MixVault

Photos: @TheMixVault

Colors

Designer to choose colors to be used in the design.

Requirements
Must have
• emphasis my logo and minimize the name/title and company information.
• SPECS:
• CMYK color mode
• High (300ppi) raster effect.
• cover bleed area
• please deliver: Illustrator file with layers and a pdf at completion.
Nice to have
• maybe include the following:
• all black background or black theme
• my work trailer (actual or cartoon) refer to Photos: @TheMixVault

```html
<!DOCTYPE html>
<html lang="en">
<head>
<meta charset="utf-8">
<title>MixVault Business Cards</title>
<link rel="stylesheet" href="https://fonts.googleapis.com/css2?family=Open+Sans:wght@400;600&display=swap">
<style>
  :root {
    --page: #2b2b2b;
    --card-white: #ffffff;
    --ink: #2a2a2a;
    --ink-soft: #444444;
    --rule: #9a9a9a;
    --logo-grey: #6e6e6e;
    --logo-light: #e2e2e2;
    --band-light: #a3a3a3;
    --band-dark: #5a5a5a;
  }
  * { margin: 0; padding: 0; box-sizing: border-box; }
  html, body {
    width: 1200px; height: 1200px; overflow: hidden;
    background: var(--page);
    font-family: "Open Sans", sans-serif;
  }
  .card {
    position: absolute;
    left: 288px;
    width: 708px; height: 402px;
    border-radius: 14px;
    overflow: hidden;
  }
  .card-front { top: 190px; background: var(--card-white); }
  .card-back  { top: 662px; }

  .front-band { position: absolute; left: 0; top: 0; width: 708px; height: 402px; }

  .brand-name {
    position: absolute;
    font-weight: 600;
    letter-spacing: 1px;
    white-space: nowrap;
  }
  .card-front .brand-name {
    left: 48px; width: 306px; top: 150px;
    font-size: 56px; color: var(--logo-grey);
    text-align: center;
  }
  .divider {
    position: absolute; left: 386px; top: 74px;
    width: 1px; height: 234px; background: var(--rule);
  }
  .person-name {
    position: absolute; left: 416px; top: 62px;
    font-size: 24px; color: var(--ink); font-weight: 400;
  }
  .person-title {
    position: absolute; left: 418px; top: 92px;
    font-size: 16px; color: var(--ink-soft);
  }
  .contact-list {
    position: absolute; left: 422px; top: 172px;
    list-style: none;
    font-size: 16px; line-height: 23px; color: var(--ink-soft);
  }
  .contact-list li { display: flex; align-items: flex-start; }
  .contact-list svg { width: 13px; height: 13px; margin: 5px 8px 0 0; flex: none; fill: var(--ink-soft); }
  .contact-list .address { line-height: 18px; margin: 3px 0 2px; }

  .scene-fill {
    position: absolute; inset: 0;
    background: linear-gradient(180deg, #8a8d93 0%, #6c6e72 22%, #3a3b3d 45%, #2b2b2c 70%, #5f6a45 86%, #7f8a63 100%);
  }
  .logo-band {
    position: absolute; left: 0; top: 100px; width: 708px; height: 186px;
    background: rgba(25, 25, 25, 0.55);
  }
  .card-back .brand-name {
    left: 0; width: 708px; top: 150px;
    font-size: 64px; color: var(--logo-light);
    text-align: center;
  }
</style>
</head>
<body>
  <section class="card card-front">
    <svg class="front-band" viewBox="0 0 708 402" aria-hidden="true">
      <defs>
        <linearGradient id="bandDark" x1="0" y1="0" x2="1" y2="0">
          <stop offset="0" stop-color="#4e4e4e"/>
          <stop offset="1" stop-color="#6d6d6d"/>
        </linearGradient>
      </defs>
      <rect x="0" y="336" width="708" height="66" fill="var(--band-light)"/>
      <rect x="0" y="336" width="708" height="3" fill="#c9c9c9"/>
      <polygon points="276,402 318,346 708,346 708,402" fill="url(#bandDark)"/>
      <polyline points="276,402 318,346 708,346" fill="none" stroke="#e6e6e6" stroke-width="2"/>
    </svg>
    <div class="brand-name">MixVault</div>
    <div class="divider"></div>
    <h1 class="person-name">Dallin Perry</h1>
    <p class="person-title">ADR Mixer</p>
    <ul class="contact-list">
      <li><svg viewBox="0 0 24 24"><path d="M6.6 10.8a15.1 15.1 0 0 0 6.6 6.6l2.2-2.2a1 1 0 0 1 1-.25 11.4 11.4 0 0 0 3.6.57 1 1 0 0 1 1 1V20a1 1 0 0 1-1 1A17 17 0 0 1 3 4a1 1 0 0 1 1-1h3.5a1 1 0 0 1 1 1 11.4 11.4 0 0 0 .57 3.6 1 1 0 0 1-.25 1z"/></svg>604.518.2093</li>
      <li><svg viewBox="0 0 24 24"><path d="M12 2a10 10 0 1 0 0 20 10 10 0 0 0 0-20zm6.9 6h-2.9a15.7 15.7 0 0 0-1.4-3.6A8 8 0 0 1 18.9 8zM12 4c.8 1.2 1.5 2.5 1.9 4h-3.8c.4-1.5 1.1-2.8 1.9-4zM4.3 14a8.2 8.2 0 0 1 0-4h3.4a16.5 16.5 0 0 0 0 4zm.8 2H8a15.7 15.7 0 0 0 1.4 3.6A8 8 0 0 1 5.1 16zM8 8H5.1a8 8 0 0 1 4.3-3.6A15.7 15.7 0 0 0 8 8zm4 12c-.8-1.2-1.5-2.5-1.9-4h3.8c-.4 1.5-1.1 2.8-1.9 4zm2.3-6H9.7a14.7 14.7 0 0 1 0-4h4.6a14.7 14.7 0 0 1 0 4zm.3 5.6A15.7 15.7 0 0 0 16 16h2.9a8 8 0 0 1-4.3 3.6zm1.7-5.6a16.5 16.5 0 0 0 0-4h3.4a8.2 8.2 0 0 1 0 4z"/></svg>www.MixVault.com</li>
      <li><svg viewBox="0 0 24 24"><path d="M12 2a7 7 0 0 0-7 7c0 5.2 7 13 7 13s7-7.8 7-13a7 7 0 0 0-7-7zm0 9.5A2.5 2.5 0 1 1 12 6.5a2.5 2.5 0 0 1 0 5z"/></svg><span class="address">248 - 5170 East Hollister<br>Vancouver, BC V5R 2J4</span></li>
      <li><svg viewBox="0 0 24 24"><rect x="3" y="3" width="18" height="18" rx="2"/></svg>Photos: @TheMixVault</li>
      <li><svg viewBox="0 0 24 24"><rect x="5" y="5" width="14" height="14"/></svg>Social: @MixVault</li>
    </ul>
  </section>

  <section class="card card-back">
    <div class="scene-fill" role="img" aria-label="Photo of the mobile recording trailer parked beside a path and lawn under a cloudy sky"></div>
    <div class="logo-band"></div>
    <div class="brand-name">MixVault</div>
  </section>
</body>
</html>
```